Lantern Harbor CD design

I need a CD cover & sleeve design for an upcoming February 2014 CD release event (at a music store). This is a collection of original songs written and sung by yours truly. Many songs are inspired by my ancestors, although there are a few songs that are just about life and love. We are all a product of our ancestry, and we carry this history in our hearts whether we think it influences us or not. This is my first CD although I've been singing and performing for over 30 years, and this body of work is where I'm at now musically and creatively. I'm proud of the effort I've made and want to present myself as someone who is real and genuine. My design style tends towards simple, clean, uncluttered lines, sans serif type faces. No loud or saturated colors please, no reds or pinks. I love the blues & greens. I have a sepia image in my head, but maybe because I've been looking at old photos of my grandparents as inspiration for the last 6 months...!

I am including two shots of me, and some old photos that could be used as a design element, but not mandatory. I wanted you to have some choices... I also have a lot of CD liner notes, but am willing to edit if I need to. This would need to be in 4 color with a sleeve that flaps open, and a lift of something similar for CD imprint. Sorry about the tight deadline, I have to get a print run done before the launch and that lead time is ridiculously tight. If you want an mp3 sample of one song I am happy to forward to give you an idea of my sound, it might help to inspire if you're a music person :-) just let me know at marenvoltatquillmaildotcom

Update for inside text: Cover photo by Arthur Penwick, others photos taken by Maren Volt.

Target Market(s)

Anyone who likes original singer / songwriter music, fellow music lovers, audience members after a performance. My influence is only in the northeast US thus far.

Industry/Entity Type

Store

Requirements
Must have
• Title of CD: Lantern Harbor

Name: Maren Volt

lower left back corner - leave 1-1/4"x1/2" room in design on back cover for UPC barcode
Nice to have
• A lighter touch, artistic vibe, softer painterly approach, Don't mind the blue / green spectrum, or a sepia toned feel. Some music folks feedback has inspired me to update this: I need o have my face on the cover! the b&w shot is a little better. And it would be nice to incorporate both sets of ancestor pictures in some way. (The faded grandma and young boy and the couple with flowers that I am holding).
Song list on the back is helpful, too.
Should not have
• No loud, saturated colors, no reds or pinks please.

```html
<!DOCTYPE html>
<html lang="en">
<head>
<meta charset="utf-8">
<title>Lantern Harbor – CD Cover</title>
<link rel="stylesheet" href="https://fonts.googleapis.com/css2?family=Federant&family=Marcellus&family=Libre+Baskerville:ital@1&display=swap">
<style>
  :root {
    --page-bg: #d9d9d9;
    --sky-pale: #d7ecf1;
    --sky-light: #a8d4e0;
    --sky-mid: #8fc0cc;
    --haze: #9fbfc0;
    --water-mid: #6f9594;
    --water-green: #5e8a80;
    --water-deep: #4a6d6a;
    --title-ink: rgba(18, 84, 116, 0.86);
    --band: #1c6782;
    --band-text: #f3f8f9;
  }
  * { box-sizing: border-box; margin: 0; padding: 0; }
  html, body {
    width: 1200px;
    height: 923px;
    overflow: hidden;
    background: var(--page-bg);
  }
  .cd-cover {
    position: absolute;
    left: 272px;
    top: 210px;
    width: 581px;
    height: 558px;
    overflow: hidden;
  }
  .cover-photo {
    position: absolute;
    inset: 0;
    background:
      radial-gradient(ellipse 60% 30% at 75% 8%, rgba(255,255,255,0.6), transparent 70%),
      radial-gradient(ellipse 80% 18% at 50% 60%, rgba(225,238,236,0.45), transparent 75%),
      radial-gradient(ellipse 70% 40% at 15% 95%, rgba(120,160,130,0.45), transparent 70%),
      linear-gradient(180deg,
        var(--sky-pale) 0%,
        var(--sky-light) 22%,
        var(--sky-mid) 40%,
        var(--haze) 55%,
        var(--water-mid) 68%,
        var(--water-green) 84%,
        var(--water-deep) 100%);
  }
  .album-title {
    position: absolute;
    left: 38px;
    top: 46px;
    width: 480px;
    font-family: "Federant", serif;
    font-weight: 400;
    font-size: 112px;
    line-height: 104px;
    letter-spacing: -2px;
    color: var(--title-ink);
    text-transform: uppercase;
    white-space: nowrap;
  }
  .volume-band {
    position: absolute;
    left: 0;
    top: 263px;
    width: 380px;
    height: 32px;
    background: var(--band);
    display: flex;
    align-items: center;
    justify-content: flex-end;
    padding-right: 12px;
  }
  .volume-label {
    font-family: "Marcellus", serif;
    font-size: 22px;
    color: var(--band-text);
    letter-spacing: 0.5px;
  }
  .credit-band {
    position: absolute;
    left: 221px;
    right: 0;
    top: 493px;
    height: 23px;
    background: var(--band);
    display: flex;
    align-items: center;
    padding-left: 8px;
  }
  .artist-credit {
    font-family: "Libre Baskerville", serif;
    font-style: italic;
    font-size: 13px;
    color: var(--band-text);
  }
</style>
</head>
<body>
  <main class="cd-cover">
    <div class="cover-photo" role="img" aria-label="Photograph of heavy rain splashing on a wet surface under soft blue light, teal and green tones"></div>
    <h1 class="album-title">Lantern<br>Harbor</h1>
    <div class="volume-band"><span class="volume-label">VOLUME ONE</span></div>
    <div class="credit-band"><span class="artist-credit">by Maren Volt , 2013</span></div>
  </main>
</body>
</html>
```